Delegate visit agenda

We need a creative, yet simple and official design for an agenda to be handed out for delegates visiting our organization. The design needs to be creative, informative and visual when possible. Flat design is desired but other options are welcomed. The agenda should be 3 pages in lengths only. Page 1 should have the company logo with an event title (with the ability to add country flag) and the dates of the event. Pages 2 should include photos of receiving delegate (e.g. VIPs) and any other relevant people. Page 3 should include agenda entries with the following information: title of entry, date and time, location, relevant pictures (e.g. a hotel or flight). The generic style of an infographic.
Updates
Project Deadline Extended
Reason: Not enough submissions received.
No optimal design (i.e. creative and attractive) received.

Brief has been updated with samples.

Target Market(s)
Very high profile people (e.g. presidents, ministers, GM,...etc.)
Industry/Entity Type
Hotel
Colors
Designer to choose colors to be used in the design.
Look and feel
Each slider illustrates characteristics of the customer's brand and the style your logo design should communicate.

```html
<!DOCTYPE html>
<html lang="en">
<head>
<meta charset="utf-8">
<title>Delegate Visit Agenda</title>
<link rel="stylesheet" href="https://fonts.googleapis.com/css2?family=Josefin+Sans:wght@600;700&display=swap">
<style>
  :root {
    --page-one: #231713;
    --page-two: #4a2600;
    --page-three: #623a12;
    --ink: #ffffff;
    --rule: #f3e9df;
    --clock: #f39a1e;
    --photo-light: #b8b8b8;
    --photo-dark: #3a3a3a;
    --photo-edge: #6a4a2a;
    --label-one: #2e211c;
    --label-two: #56300b;
    --label-three: #6d4419;
  }
  * { box-sizing: border-box; margin: 0; padding: 0; }
  html, body { width: 1200px; height: 800px; overflow: hidden; }
  body { font-family: "Josefin Sans", sans-serif; color: var(--ink); }
  .agenda { position: relative; width: 1200px; height: 800px; display: flex; }
  .page { position: relative; width: 400px; height: 800px; }
  .page--cover { background: var(--page-one); }
  .page--people { background: var(--page-two); }
  .page--entries { background: var(--page-three); }

  .event-title {
    position: absolute; top: 130px; left: 0; width: 400px;
    text-align: center; font-weight: 700; font-size: 34px; line-height: 44px;
  }
  .event-date {
    position: absolute; top: 632px; left: 56px;
    display: flex; align-items: center; gap: 10px;
    font-weight: 700; font-size: 18px;
  }
  .event-date svg { width: 38px; height: 38px; }

  .photo {
    position: absolute;
    background: radial-gradient(circle at 50% 40%, var(--photo-light), var(--photo-dark) 75%);
    border: 1px solid var(--photo-edge);
  }
  .host-photo { left: 41px; width: 110px; height: 110px; }
  .host-name {
    position: absolute; left: 170px; font-weight: 700; font-size: 19px; line-height: 25px;
  }
  .guest-photo { width: 46px; height: 46px; }
  .guest-name {
    position: absolute; font-weight: 700; font-size: 13px; line-height: 16px; letter-spacing: 0.5px;
  }

  .field-label { position: absolute; left: 45px; font-weight: 700; font-size: 18px; }
  .field-rule { position: absolute; left: 38px; width: 324px; height: 2px; background: var(--rule); }

  .page-label {
    position: absolute; bottom: 28px; left: 0; width: 400px; text-align: center;
    font-weight: 700; font-size: 34px;
  }
  .page--cover .page-label { color: var(--label-one); }
  .page--people .page-label { color: var(--label-two); }
  .page--entries .page-label { color: var(--label-three); }
</style>
</head>
<body>
<main class="agenda">
  <section class="page page--cover">
    <h1 class="event-title">Graphic Design Job:<br>Delegate Visit Agenda</h1>
    <p class="event-date">
      <svg viewBox="0 0 38 38" aria-hidden="true">
        <circle cx="19" cy="19" r="18" fill="var(--clock)"/>
        <circle cx="19" cy="19" r="13" fill="#fff"/>
        <path d="M19 10 V19 L25 23" stroke="#555" stroke-width="2" fill="none" stroke-linecap="round"/>
      </svg>
      Tuesday, December 23, 2014
    </p>
    <p class="page-label">demo page1</p>
  </section>

  <section class="page page--people">
    <div class="photo host-photo" style="top:224px" role="img" aria-label="Portrait of Alex Alexia"></div>
    <p class="host-name" style="top:262px">Alex Alexia<br>Manager</p>
    <div class="photo host-photo" style="top:341px" role="img" aria-label="Portrait of Ashley Ashton"></div>
    <p class="host-name" style="top:379px">Ashley Ashton<br>Operation Manager</p>
    <div class="photo host-photo" style="top:458px" role="img" aria-label="Portrait of Jack Jackson"></div>
    <p class="host-name" style="top:496px">Jack Jackson<br>Support Manager</p>

    <div class="photo guest-photo" style="left:41px;top:586px" role="img" aria-label="Delegate portrait"></div>
    <p class="guest-name" style="left:97px;top:595px">XYZ<br>XYZYZ</p>
    <div class="photo guest-photo" style="left:163px;top:586px" role="img" aria-label="Delegate portrait"></div>
    <p class="guest-name" style="left:215px;top:595px">XYZ<br>XYZYZ</p>
    <div class="photo guest-photo" style="left:277px;top:586px" role="img" aria-label="Delegate portrait"></div>
    <p class="guest-name" style="left:330px;top:595px">XYZ<br>XYZYZ</p>
    <div class="photo guest-photo" style="left:41px;top:649px" role="img" aria-label="Delegate portrait"></div>
    <p class="guest-name" style="left:98px;top:657px">XYZ<br>XYZYZ</p>
    <div class="photo guest-photo" style="left:163px;top:649px" role="img" aria-label="Delegate portrait"></div>
    <p class="guest-name" style="left:216px;top:657px">XYZ<br>XYZYZ</p>
    <div class="photo guest-photo" style="left:277px;top:649px" role="img" aria-label="Delegate portrait"></div>
    <p class="guest-name" style="left:331px;top:657px">XYZ<br>XYZYZ</p>
    <p class="page-label">demo page2</p>
  </section>

  <section class="page page--entries">
    <p class="field-label" style="top:567px">Date / Time</p>
    <div class="field-rule" style="top:622px"></div>
    <p class="field-label" style="top:666px">Location</p>
    <div class="field-rule" style="top:721px"></div>
    <p class="page-label">demo page3</p>
  </section>
</main>
</body>
</html>
```